8 scene designs needed for a cool motion graphics video

We need a storyboard created for motion-graphics product video. The storyboard will need to consist of EIGHT creative and beautifully designed templates or what we call – scenes.
Once you deliver the scenes, we’ll turn them into a product video template targeting small to medium-sized businesses in North America.
Check out ‘Sample Storyboard.pdf’ – we are looking for something like this but BETTER!
While we strongly welcome creativity, here’s a guide for the 8 scenes we’re looking for.
Scene #1 - Title/Introduction. All good videos start with a catchy introduction. At minimum, this scene would need to include a placeholder for a company’s logo, tagline, maybe even an image of their business.
Scene #2 – Product Features 1. This is where the business would promote its products – cameras, bikes, shoes, jackets, electronics, jewellery, doesn’t matter. This scene would generally consist of placeholders for the following product information: product images, product name, product features, price and benefits.
Scene #3 – Product Features 2. See above. We are just looking for TWO product promo scenes.
Scene #4 – Promotion or Special Offer. Most businesses sell using special offers or promotions – we want deliver a cool scene to showcase this. It would contain an image of the product ‘on sale’, a description, a sale or special image, etc.
Scene #5 - Product Rating. This is pretty straight forward, using stars, ‘thumbs up’ or whatever we want businesses to be able to show how highly their product(s) have been rated. It should also contain a testimonial/review.
Scene #6 – Product Reviews or Testimonials. This is pretty straight forward as well – a scene where businesses can show a few customer testimonials; maybe in conjunction with an image or some other cool graphics like a call-out? Your call there. Same as above but minus the ratings.
Scene #7 – Map/Contact Us. This scene would generally consist of a map locating the business’s address as well as other contact details.
Scene #8 – End Scene/Conclusion. Finally, we want to close things down in style. Here, a business will want to reinforce their brand (usually their logo) and have some closing Call-To-Action, a button or something to ‘buy now’, visit my website, call me, etc. These buttons will be clickable!
Small businesses will be buying this video to promote themselves
Business

```html
<!DOCTYPE html>
<html lang="en">
<head>
<meta charset="utf-8">
<title>Bright Studio – Title Scene</title>
<link rel="stylesheet" href="https://fonts.googleapis.com/css2?family=Russo+One&family=Dancing+Script:wght@500&display=swap">
<style>
  :root {
    --wall-bright: #ff0818;
    --wall-deep: #8c0006;
    --drape-light: #ffffff;
    --drape-shade: #b9bde8;
    --floor-light: #b01a08;
    --floor-deep: #3a0a06;
    --sign-top-a: #7a3bd0;
    --sign-top-b: #e0389a;
    --sign-edge: #3d6fe0;
    --band-blue: #1a2cb0;
    --band-line: #6a86f0;
    --name-ink: #222226;
    --tagline-ink: #ffffff;
    --cursor-face: #3552b0;
    --cursor-side: #6f8190;
    --cursor-rim: #1e78b4;
  }
  * { box-sizing: border-box; margin: 0; padding: 0; }
  html, body { width: 1200px; height: 718px; overflow: hidden; background: #ffffff; }
  .scene { position: relative; width: 1200px; height: 718px; overflow: hidden; }
  .scene-art { position: absolute; inset: 0; }
  .brand-name {
    position: absolute;
    left: 430px; top: 128px;
    width: 360px;
    font-family: "Russo One", sans-serif;
    font-size: 46px;
    line-height: 58px;
    letter-spacing: 3px;
    text-align: center;
    color: var(--name-ink);
  }
  .brand-dot {
    position: absolute;
    left: 350px; top: 148px;
    width: 50px; height: 50px;
    border-radius: 50%;
    background: var(--name-ink);
  }
  .tagline {
    position: absolute;
    left: 197px; top: 268px;
    width: 816px;
    font-family: "Dancing Script", cursive;
    font-weight: 500;
    font-size: 36px;
    line-height: 60px;
    text-align: center;
    color: var(--tagline-ink);
  }
</style>
</head>
<body>
<main class="scene">
  <svg class="scene-art" width="1200" height="718" viewBox="0 0 1200 718" xmlns="http://www.w3.org/2000/svg">
    <defs>
      <radialGradient id="wallGlow" cx="0.5" cy="0.1" r="0.8">
        <stop offset="0" stop-color="var(--wall-bright)"/>
        <stop offset="1" stop-color="var(--wall-deep)"/>
      </radialGradient>
      <linearGradient id="drapeLeft" x1="0" x2="1">
        <stop offset="0" stop-color="var(--drape-light)"/>
        <stop offset="1" stop-color="var(--drape-shade)"/>
      </linearGradient>
      <linearGradient id="drapeRight" x1="1" x2="0">
        <stop offset="0" stop-color="var(--drape-light)"/>
        <stop offset="1" stop-color="var(--drape-shade)"/>
      </linearGradient>
      <radialGradient id="floorGlow" cx="0.55" cy="0.45" r="0.7">
        <stop offset="0" stop-color="var(--floor-light)"/>
        <stop offset="1" stop-color="var(--floor-deep)"/>
      </radialGradient>
      <linearGradient id="signTop" x1="0" x2="1">
        <stop offset="0" stop-color="var(--sign-top-a)"/>
        <stop offset="0.6" stop-color="var(--sign-top-b)"/>
        <stop offset="1" stop-color="var(--sign-top-a)"/>
      </linearGradient>
    </defs>

    <rect class="backdrop-wall" x="165" y="0" width="880" height="420" fill="url(#wallGlow)" role="img" aria-label="Red wall with floral swirl ornaments"/>

    <rect class="drape drape-left" x="0" y="0" width="170" height="718" fill="url(#drapeLeft)" role="img" aria-label="White drape with pink roses"/>
    <rect class="drape drape-right" x="1040" y="0" width="160" height="718" fill="url(#drapeRight)" role="img" aria-label="White drape with pink roses"/>

    <path class="stage-floor" d="M170 418 Q600 392 1040 405 Q1110 560 1200 718 L0 718 Q110 560 170 418 Z" fill="url(#floorGlow)" role="img" aria-label="Swirling red floor pattern"/>

    <g class="title-sign">
      <polygon class="sign-top" points="335,124 868,124 1013,260 197,260" fill="url(#signTop)" stroke="var(--sign-edge)" stroke-width="6" stroke-linejoin="round"/>
      <rect class="sign-band" x="197" y="262" width="816" height="74" fill="var(--band-blue)"/>
      <line x1="197" y1="268" x2="1013" y2="268" stroke="var(--band-line)" stroke-width="2"/>
      <line x1="197" y1="274" x2="1013" y2="274" stroke="var(--band-line)" stroke-width="1"/>
      <line x1="197" y1="324" x2="1013" y2="324" stroke="var(--band-line)" stroke-width="1"/>
      <line x1="197" y1="330" x2="1013" y2="330" stroke="var(--band-line)" stroke-width="2"/>
    </g>

    <g class="pointer-arrow">
      <polygon class="pointer-side" points="889,317 1056,424 996,452 1074,527 1046,557 966,479 921,517" fill="var(--cursor-side)"/>
      <polygon class="pointer-face" points="883,303 1050,412 990,440 1068,515 1040,545 960,467 915,505" fill="var(--cursor-face)" stroke="var(--cursor-rim)" stroke-width="5" stroke-linejoin="round"/>
    </g>
  </svg>

  <span class="brand-dot"></span>
  <h1 class="brand-name">BRIGHT<br>STUDIO</h1>
  <p class="tagline">Complete Satisfaction</p>
</main>
</body>
</html>
```